Wedding Videography Wordpress Website Theme

We need a modern and high-end website look for our wedding video and film business. We film weddings all over the United Kingdom and at European destinations so need something to reflect our work. The website should be visually stunning with images and videos being the focal point as this is what our services are.

The current website is www.brennolwick.com so you will be able to see our brand.

My Instagram is www.instagram.com/brennolwickfilms so a new design should link in with this idea.

We need the following pages designed by the winning designer

1 - Homepage
2 - Films Index Page
3 - Testimonials
4 - Prices
5 - Reviews
6 - Meet Tobin (About)
7 - Contact
8 - Blog Index
9 - Blog Page

All pages must be consistent so have a similar style.

Pages on menu:
Meet Tobin
Videos
Packages
Testimionials
Journal (Blog)
Contact

We require a responsive look too. Over 90% of our visitors access the website via their mobile devices.

```html
<!DOCTYPE html>
<html lang="en">
<head>
<meta charset="utf-8">
<title>Tobin Brennolwick Wedding Films</title>
<link href="https://fonts.googleapis.com/css2?family=Josefin+Sans:wght@400;600;700&family=Roboto:wght@400;500;700&family=Great+Vibes&display=swap" rel="stylesheet">
<style>
:root{
  --gold:#a8884f;
  --gold-light:#c9a866;
  --ink:#2d2a28;
  --text:#555;
  --footer:#4b403c;
  --white:#fff;
  --field:#e2e2e2;
}
*{box-sizing:border-box;margin:0;padding:0}
html,body{width:1200px;height:5074px;overflow:hidden}
body{position:relative;font-family:Roboto,Arial,sans-serif;color:var(--text);background:var(--white)}
.block{position:absolute;left:0;width:1200px}
.photo{position:absolute}
.btn{position:absolute;display:inline-flex;align-items:center;gap:8px;background:var(--gold);color:var(--white);font:700 13px Roboto,sans-serif;letter-spacing:.3px;text-transform:uppercase;padding:0 22px;height:42px}
.btn .dot{width:13px;height:13px;border-radius:50%;background:var(--white);display:inline-flex;align-items:center;justify-content:center}
.btn .dot::after{content:"";border-left:5px solid var(--gold);border-top:3.5px solid transparent;border-bottom:3.5px solid transparent;margin-left:1px}
/* header */
.brand{position:absolute;left:144px;top:18px;width:152px;text-align:center;color:var(--ink);white-space:nowrap}
.brand .sq{width:26px;height:26px;border:2px solid var(--gold);margin:0 auto 7px;transform:rotate(45deg)}
.brand .name{font:600 13px "Josefin Sans",sans-serif;letter-spacing:1.5px}
.brand .sub{font:400 7px "Josefin Sans",sans-serif;letter-spacing:3px;margin-top:2px}
.nav{position:absolute;left:386px;top:44px;display:flex;gap:25px;font-size:13px;color:var(--ink)}
.nav-cta{position:absolute;left:919px;top:33px;width:137px;height:40px;background:var(--gold);color:var(--white);font-size:13px;display:flex;align-items:center;justify-content:center}
/* hero */
.hero h1{position:absolute;left:144px;top:238px;font:600 50px "Josefin Sans",sans-serif;color:var(--white);letter-spacing:1px;white-space:nowrap}
.hero .script{position:absolute;left:144px;top:296px;font:22px "Great Vibes",cursive;color:var(--white)}
.hero p{position:absolute;left:144px;top:350px;width:420px;font-size:14px;line-height:23px;color:var(--white)}
/* intro */
.intro h2{position:absolute;left:0;width:1200px;top:78px;text-align:center;font:600 31px/33px "Josefin Sans",sans-serif;color:var(--white);text-transform:uppercase}
.intro .copy{position:absolute;left:320px;width:560px;top:168px;text-align:center;font-size:12px;line-height:22px;color:var(--white)}
.intro .copy p{margin-bottom:8px}
/* section titles */
.sec-title{position:absolute;left:0;width:1200px;text-align:center}
.sec-title .mark{width:22px;height:22px;border:2px solid var(--gold);transform:rotate(45deg);margin:0 auto 18px}
.sec-title h2{font:600 35px "Josefin Sans",sans-serif;color:var(--ink);text-transform:uppercase;letter-spacing:1px}
/* packages */
.pkg-card{position:absolute;top:1379px;height:381px;overflow:hidden}
.pkg-side-label{position:absolute;top:170px;font:500 10px Roboto,sans-serif;letter-spacing:3px;color:var(--white);writing-mode:vertical-rl}
.pkg-frame{position:absolute;left:36px;top:36px;right:36px;bottom:36px;border:2px solid var(--white)}
.pkg-name{position:absolute;left:0;right:0;top:152px;text-align:center;font:600 28px "Josefin Sans",sans-serif;color:var(--white)}
.pkg-price{position:absolute;left:0;right:0;top:192px;text-align:center;font:500 22px Roboto,sans-serif;color:var(--gold-light)}
.dots{position:absolute;top:1802px;left:566px;display:flex;gap:4px}
.dots span{width:9px;height:9px;border-radius:50%;border:1px solid var(--gold)}
.dots span:first-child{background:var(--gold)}
/* about */
.about h2{position:absolute;left:144px;top:82px;width:600px;font:600 29px/38px "Josefin Sans",sans-serif;color:var(--white);text-transform:uppercase}
.about .copy{position:absolute;left:144px;top:297px;width:570px;font-size:12px;line-height:21px;color:var(--white)}
.about .copy p{margin-bottom:12px}
/* testimonial */
.testi .wrap{position:absolute;left:470px;width:580px;top:96px;text-align:center;color:var(--white)}
.testi .kicker{font:600 15px/21px Roboto,sans-serif;text-transform:uppercase}
.testi .names{font:600 36px "Josefin Sans",sans-serif;margin:18px 0 16px;letter-spacing:1px}
.testi .quote{font-size:12px;line-height:22px;font-style:italic}
.testi .venue{font:500 16px Roboto,sans-serif;margin-top:16px;font-style:italic}
/* contact */
.chat h2{position:absolute;left:144px;top:100px;font:600 36px "Josefin Sans",sans-serif;color:var(--ink);text-transform:uppercase;letter-spacing:1px}
.chat .lead{position:absolute;left:144px;top:166px;font-size:13px;line-height:22px;color:var(--ink)}
.chat .lead b{color:var(--gold);font-weight:500}
.field{position:absolute}
.field label{display:block;font:500 13px Roboto,sans-serif;color:var(--ink);margin-bottom:14px}
.field .box{height:43px;border:1px solid var(--field);background:var(--white);font-size:11px;color:#999;display:flex;align-items:center;justify-content:space-between;padding:0 16px}
.caret{border-top:5px solid #777;border-left:4px solid transparent;border-right:4px solid transparent}
/* footer */
.footer{background:var(--footer);color:var(--white)}
.f-brand{position:absolute;left:134px;top:62px;width:250px;text-align:center;white-space:nowrap}
.f-brand .sq{width:46px;height:46px;border:3px solid var(--gold-light);margin:6px auto 20px;transform:rotate(45deg)}
.f-brand .name{font:600 19px "Josefin Sans",sans-serif;letter-spacing:2px}
.f-brand .sub{font:400 10px "Josefin Sans",sans-serif;letter-spacing:5px;margin:3px 0 20px}
.f-brand .small{font-size:12px;line-height:22px}
.f-brand .small .cs{color:var(--gold-light)}
.f-col{position:absolute;top:70px}
.f-col h4{font:600 15px Roboto,sans-serif;color:var(--gold-light);margin-bottom:18px}
.f-col ul{list-style:none;font-size:12px;line-height:25px}
.thumbs{display:grid;grid-template-columns:repeat(3,48px);gap:14px 14px}
.thumbs div{height:40px}
.sub-form{margin-top:20px;width:232px;height:40px;border-radius:20px;background:var(--white);position:relative;font-size:10px;color:#999;padding:14px 20px}
.sub-form span{position:absolute;right:0;top:0;height:40px;width:115px;border-radius:20px;background:var(--gold);color:var(--white);font:700 14px Roboto,sans-serif;display:flex;align-items:center;justify-content:center}
.social{display:flex;gap:8px;align-items:center;font-size:11px;margin-top:18px}
.social i{width:8px;height:8px;border-radius:50%;background:var(--white);display:inline-block}
.f-bottom{position:absolute;top:343px;left:144px;width:910px;font-size:11px;display:flex;justify-content:space-between}
.badges{position:absolute;left:558px;top:320px;display:flex;gap:8px}
.badges div{width:42px;height:42px;border-radius:50%}
</style>
</head>
<body>

<!-- Hero -->
<section class="block hero" style="top:0;height:655px">
  <div class="photo" role="img" aria-label="Bride and groom embracing in a rose garden" style="inset:0;background:
    radial-gradient(ellipse 150px 230px at 810px 450px,rgba(238,232,224,.95),rgba(238,232,224,0) 100%),
    radial-gradient(ellipse 110px 250px at 930px 360px,rgba(32,36,58,.9),rgba(32,36,58,0) 100%),
    radial-gradient(ellipse 70px 60px at 860px 190px,rgba(226,190,160,.85),rgba(226,190,160,0) 100%),
    radial-gradient(ellipse 70px 55px at 780px 480px,rgba(196,150,160,.8),rgba(196,150,160,0) 100%),
    radial-gradient(ellipse 260px 140px at 1100px 560px,rgba(150,80,100,.35),rgba(150,80,100,0) 100%),
    radial-gradient(ellipse 420px 260px at 250px 520px,rgba(70,80,55,.9),rgba(70,80,55,0) 100%),
    linear-gradient(180deg,#6e7a62 0%,#4c5a3c 45%,#3b4530 100%)"></div>
  <div class="photo" style="inset:0;background:linear-gradient(180deg,rgba(255,255,255,.92) 0,rgba(255,255,255,.6) 70px,rgba(255,255,255,0) 150px)"></div>
  <div class="brand">
    <div class="sq"></div>
    <div class="name">TOBIN BRENNOLWICK</div>
    <div class="sub">WEDDING FILMS</div>
  </div>
  <nav class="nav"><span>Meet Tobin</span><span>Videos</span><span>Packages</span><span>Testimonials</span><span>Journal</span><span>Contact</span></nav>
  <div class="nav-cta">Get In Touch</div>
  <h1>TOBIN BRENNOLWICK</h1>
  <div class="script">North East and Yorkshire Wedding Videographer</div>
  <p>On the day Tobin and Rowan were great in making us feel comfortable and we hardly realised</p>
  <div class="btn" style="left:144px;top:430px">Contact Us <span class="dot"></span></div>
</section>

<!-- Intro -->
<section class="block intro" style="top:655px;height:555px">
  <div class="photo" role="img" aria-label="Bride and groom walking hand in hand across a lawn" style="inset:0;background:
    radial-gradient(ellipse 170px 260px at 250px 350px,rgba(240,236,228,.95),rgba(240,236,228,0) 100%),
    radial-gradient(ellipse 60px 50px at 240px 150px,rgba(222,190,150,.8),rgba(222,190,150,0) 100%),
    radial-gradient(ellipse 130px 200px at 960px 440px,rgba(34,40,78,.95),rgba(34,40,78,0) 100%),
    radial-gradient(ellipse 55px 50px at 960px 250px,rgba(215,170,140,.8),rgba(215,170,140,0) 100%),
    linear-gradient(180deg,#3f4834 0%,#57703a 35%,#6e9a38 70%,#5e8a30 100%)"></div>
  <div class="photo" style="inset:0;background:radial-gradient(ellipse 420px 260px at 600px 240px,rgba(0,0,0,.28),rgba(0,0,0,0))"></div>
  <h2>Your wedding day is the most important<br>day of your life. . .</h2>
  <div class="copy">
    <p>The celebration of your love story… and you'll want to remember it for the rest of your lives.</p>
    <p>Your wedding film is the best way to keep this day alive forever … a newlywed's gift that keeps giving … an infinite reminder of those special moments and memories.</p>
    <p>Everything about your wedding day belongs to you, the couple. Your story. Your vibe. Your friends and family. Your pre-wedding jitters.</p>
  </div>
  <div class="btn" style="left:515px;top:337px">Learn More <span class="dot"></span></div>
</section>

<!-- Packages -->
<div class="sec-title" style="top:1260px"><div class="mark"></div><h2>Our Packages</h2></div>
<div class="pkg-card" style="left:0;width:280px">
  <div class="photo" role="img" aria-label="Black and white photo of a laughing bride" style="inset:0;background:
    radial-gradient(ellipse 140px 200px at 120px 260px,#f2f2f2,rgba(242,242,242,0) 100%),
    radial-gradient(ellipse 90px 90px at 80px 80px,#c8c8c8,rgba(200,200,200,0) 100%),
    linear-gradient(135deg,#4a4a4a,#8a8a8a 60%,#3a3a3a)"></div>
  <div class="pkg-side-label" style="right:10px">PREV</div>
</div>
<div class="pkg-card" style="left:320px;width:560px">
  <div class="photo" role="img" aria-label="Couple in an autumn garden" style="inset:0;background:
    radial-gradient(ellipse 110px 170px at 410px 290px,rgba(235,228,222,.95),rgba(235,228,222,0) 100%),
    radial-gradient(ellipse 90px 170px at 210px 290px,rgba(40,40,55,.95),rgba(40,40,55,0) 100%),
    radial-gradient(ellipse 180px 90px at 300px 360px,rgba(170,90,150,.55),rgba(170,90,150,0) 100%),
    radial-gradient(ellipse 300px 160px at 120px 60px,rgba(225,120,40,.9),rgba(225,120,40,0) 100%),
    radial-gradient(ellipse 260px 150px at 480px 60px,rgba(200,90,30,.85),rgba(200,90,30,0) 100%),
    linear-gradient(180deg,#9c5a26,#6e6a3a 60%,#5b6a3a)"></div>
  <div class="photo" style="inset:0;background:rgba(0,0,0,.22)"></div>
  <div class="pkg-frame"></div>
  <div class="pkg-name">GOLD WEDDING FILM</div>
  <div class="pkg-price">From £1,800</div>
</div>
<div class="pkg-card" style="left:920px;width:280px">
  <div class="photo" role="img" aria-label="Black and white photo of a couple hugging" style="inset:0;background:
    radial-gradient(ellipse 100px 170px at 200px 250px,#1e1e1e,rgba(30,30,30,0) 100%),
    radial-gradient(ellipse 90px 120px at 90px 230px,#e4e4e4,rgba(228,228,228,0) 100%),
    linear-gradient(135deg,#bdbdbd,#6a6a6a 60%,#2f2f2f)"></div>
  <div class="pkg-side-label" style="left:10px">NEXT</div>
</div>
<div class="dots"><span></span><span></span><span></span><span></span><span></span></div>

<!-- Videos -->
<div class="sec-title" style="top:1888px"><div class="mark"></div><h2>Our Videos</h2></div>
<div class="photo" role="img" aria-label="Groom and bride by a window" style="left:144px;top:2003px;width:450px;height:219px;background:
  radial-gradient(ellipse 60px 110px at 160px 150px,#1d2030,rgba(29,32,48,0) 100%),
  radial-gradient(ellipse 70px 110px at 290px 140px,#e8e4dc,rgba(232,228,220,0) 100%),
  linear-gradient(90deg,#5a564e 0%,#c9c4b8 40%,#d8d3c8 60%,#4b4740 100%)"></div>
<div class="photo" role="img" aria-label="Guests throwing confetti" style="left:603px;top:2003px;width:451px;height:219px;background:
  radial-gradient(ellipse 50px 90px at 120px 150px,#c7cec2,rgba(199,206,194,0) 100%),
  radial-gradient(ellipse 60px 100px at 220px 140px,#2a2c33,rgba(42,44,51,0) 100%),
  linear-gradient(180deg,#4a5a38 0%,#7c8570 45%,#9a968c 100%)"></div>
<div class="photo" role="img" aria-label="Aerial view of a country church" style="left:144px;top:2233px;width:299px;height:199px;background:
  radial-gradient(ellipse 20px 24px at 150px 130px,#f0ede6,rgba(240,237,230,0) 100%),
  linear-gradient(180deg,#3c5f97 0,#8fa9c8 22%,#4d6a3a 30%,#34502a 65%,#26391c 100%)"></div>
<div class="photo" role="img" aria-label="Couple under string lights" style="left:454px;top:2233px;width:291px;height:199px;background:
  radial-gradient(ellipse 60px 60px at 190px 120px,#d9a37a,rgba(217,163,122,0) 100%),
  radial-gradient(ellipse 60px 100px at 100px 150px,#141414,rgba(20,20,20,0) 100%),
  linear-gradient(180deg,#1a1512,#3a2a20 60%,#5a4030)"></div>
<div class="photo" role="img" aria-label="Bride with guests outdoors" style="left:756px;top:2233px;width:298px;height:199px;background:
  radial-gradient(ellipse 70px 80px at 80px 130px,#f3f0ea,rgba(243,240,234,0) 100%),
  radial-gradient(ellipse 60px 90px at 210px 130px,#5b6270,rgba(91,98,112,0) 100%),
  linear-gradient(180deg,#c6b991,#8d8a6d 55%,#6e6a4a)"></div>
<div class="photo" role="img" aria-label="Bride under confetti" style="left:144px;top:2443px;width:180px;height:218px;background:
  radial-gradient(ellipse 50px 80px at 100px 140px,#f0ece6,rgba(240,236,230,0) 100%),
  linear-gradient(135deg,#2e2924,#6a5e52 70%,#3a332c)"></div>
<div class="photo" role="img" aria-label="Bride and groom walking through confetti" style="left:327px;top:2443px;width:267px;height:218px;background:
  radial-gradient(ellipse 55px 90px at 70px 150px,#efe9e0,rgba(239,233,224,0) 100%),
  radial-gradient(ellipse 50px 100px at 170px 140px,#3a4660,rgba(58,70,96,0) 100%),
  linear-gradient(135deg,#3b3530,#8f8274 60%,#4a4038)"></div>
<div class="photo" role="img" aria-label="Couple about to kiss at dusk" style="left:603px;top:2443px;width:451px;height:218px;background:
  radial-gradient(ellipse 50px 50px at 250px 110px,#b89e80,rgba(184,158,128,0) 100%),
  radial-gradient(ellipse 90px 100px at 120px 150px,#0e0e0c,rgba(14,14,12,0) 100%),
  linear-gradient(135deg,#56553f,#26261f 60%,#121210)"></div>
<div class="btn" style="left:503px;top:2712px;height:44px">View All Videos <span class="dot"></span></div>

<!-- About -->
<section class="block about" style="top:2847px;height:566px">
  <div class="photo" role="img" aria-label="Groom kissing bride's forehead in a park" style="inset:0;background:
    radial-gradient(ellipse 110px 250px at 960px 340px,#ece7df,rgba(236,231,223,0) 100%),
    radial-gradient(ellipse 90px 240px at 850px 320px,#1f2a48,rgba(31,42,72,0) 100%),
    radial-gradient(ellipse 350px 200px at 300px 200px,#7c7b62,rgba(124,123,98,0) 100%),
    linear-gradient(180deg,#6a6b58 0%,#59623f 60%,#4d5b34 100%)"></div>
  <div class="photo" style="inset:0;background:linear-gradient(90deg,rgba(0,0,0,.4),rgba(0,0,0,0) 65%)"></div>
  <h2>Tobin Brennolwick, a trusted and acclaimed wedding filmmaker based in the North East and Yorkshire, has more than 20 years of filmmaking experience.</h2>
  <div class="copy">
    <p>From beautiful barns and luxurious country hotels to sun-drenched Greek Islands and ancient Italian abbeys, he has filmed all kinds of unforgettable weddings.</p>
    <p>If you're looking for a highly experienced wedding videographer who focuses on your story, the goosebump moments and the emotions filling the room as you entertain your guests, then get in touch with Tobin today.</p>
  </div>
  <div class="btn" style="left:144px;top:438px;height:44px">Learn More <span class="dot"></span></div>
</section>

<!-- Testimonial -->
<section class="block testi" style="top:3413px;height:412px">
  <div class="photo" role="img" aria-label="Aerial view of a couple lying in a golden wheat field" style="inset:0;background:
    radial-gradient(ellipse 70px 100px at 330px 260px,#f2efe8,rgba(242,239,232,0) 100%),
    radial-gradient(ellipse 60px 60px at 280px 150px,#2a2a2a,rgba(42,42,42,0) 100%),
    repeating-linear-gradient(115deg,rgba(0,0,0,.08) 0 6px,rgba(255,255,255,0) 6px 14px),
    linear-gradient(135deg,#9a7838,#6a4c22 50%,#8a6a30)"></div>
  <div class="photo" style="inset:0;background:rgba(0,0,0,.22)"></div>
  <div class="wrap">
    <div class="kicker">North East &amp; Yorkshire Wedding Videographer<br>Video Testimonial</div>
    <div class="names">ISLA + OWEN</div>
    <div class="quote">We Have A Really Emotional Video For Our Wedding. It Is A Beauty Video That Is Going To Stay With Us For The Rest Of Our Lives. Tobin Was Everywhere But You Couldn't Tell He Was There. He Was A Really Fun Guy And We Now Consider Him A Friend.</div>
    <div class="venue">Married At Villa Serena, Umbria, Italy</div>
  </div>
</section>

<!-- Contact -->
<section class="block chat" style="top:3825px;height:875px">
  <div class="photo" role="img" aria-label="Silhouette of a couple kissing in black and white" style="left:560px;top:0;width:640px;height:875px;background:
    radial-gradient(ellipse 150px 330px at 420px 450px,#121212,rgba(18,18,18,0) 100%),
    radial-gradient(ellipse 130px 300px at 260px 470px,#2a2a2a,rgba(42,42,42,0) 100%),
    linear-gradient(90deg,#fff 0%,#f4f4f4 30%,#cfcfcf 60%,#e6e6e6 100%)"></div>
  <div class="photo" style="left:0;top:760px;width:1200px;height:115px;background:linear-gradient(180deg,rgba(0,0,0,0),#1f1f1f)"></div>
  <h2>Ready for a chat?</h2>
  <div class="lead">Then give me a call on <b>07700 900214</b> or email me at <b>films@brennolwick.com</b><br>and I'll respond in a couple of hours or so.</div>
  <div class="field" style="left:144px;top:228px;width:565px"><label>How Did You Hear About My Wedding Films?</label><div class="box">Choose your option <span class="caret"></span></div></div>
  <div class="field" style="left:144px;top:325px;width:268px"><label>First Name *</label><div class="box">Choose your option</div></div>
  <div class="field" style="left:441px;top:325px;width:268px"><label>Last Name *</label><div class="box">Choose your option</div></div>
  <div class="field" style="left:144px;top:421px;width:268px"><label>Email Address *</label><div class="box">Choose your option</div></div>
  <div class="field" style="left:441px;top:421px;width:268px"><label>Phone Number *</label><div class="box">Choose your option</div></div>
  <div class="field" style="left:144px;top:518px;width:268px"><label>When Is Your Wedding Day?</label><div class="box">Select Date
    <svg width="12" height="12" viewBox="0 0 12 12"><rect x="1" y="2" width="10" height="9" fill="none" stroke="#777"/><line x1="1" y1="5" x2="11" y2="5" stroke="#777"/></svg></div></div>
  <div class="field" style="left:441px;top:518px;width:268px"><label>What Time Is Your Wedding Ceremony?</label><div class="box">Wedding Time</div></div>
  <div class="field" style="left:144px;top:614px;width:565px"><label>What Are You Planning For Your Wedding Day?</label><div class="box">Are you having readings and speeches etc</div></div>
  <div class="btn" style="left:144px;top:738px;height:44px">Submit Now <span class="dot"></span></div>
</section>

<!-- Footer -->
<footer class="block footer" style="top:4700px;height:374px">
  <div class="f-brand">
    <div class="sq"></div>
    <div class="name">TOBIN BRENNOLWICK</div>
    <div class="sub">WEDDING FILMS</div>
    <div class="small"><span class="cs">Customer Service</span><br>07700 900214<br>films@brennolwick.com</div>
  </div>
  <div class="f-col" style="left:422px"><h4>Categories</h4><ul><li>Meet Tobin</li><li>Videos</li><li>Packages</li><li>Testimonials</li><li>Journal</li><li>Contact</li></ul></div>
  <div class="f-col" style="left:558px"><h4>Follow Us</h4>
    <div class="thumbs" role="img" aria-label="Grid of recent wedding photos">
      <div style="background:linear-gradient(135deg,#d8d2c6,#5a5248)"></div>
      <div style="background:linear-gradient(135deg,#3a3f55,#b9ab96)"></div>
      <div style="background:linear-gradient(135deg,#6a7a4a,#e2dccf)"></div>
      <div style="background:linear-gradient(135deg,#7f9a4a,#3a4a2a)"></div>
      <div style="background:linear-gradient(135deg,#e8e3da,#4a5a70)"></div>
      <div style="background:linear-gradient(135deg,#2a2a30,#a49a88)"></div>
      <div style="background:linear-gradient(135deg,#cfc8bb,#3b3f58)"></div>
      <div style="background:linear-gradient(135deg,#4a6a3a,#d8d4ca)"></div>
      <div style="background:linear-gradient(135deg,#5a4a70,#e6e0d6)"></div>
    </div>
  </div>
  <div class="f-col" style="left:778px;width:280px"><h4>Subscribe for Updates</h4>
    <div style="font-size:12px;line-height:20px">Subscribe to our Newsletter to receive updates, access to exclusive deals, and more.</div>
    <div class="sub-form">Email Address<span>SIGN UP</span></div>
    <div class="social">Contact With Us: <i></i><i></i><i></i><i></i></div>
  </div>
  <div class="badges"><div style="background:#1c3f7a"></div><div style="background:#e7d36a"></div></div>
  <div class="f-bottom"><span>© brennolwick 2022 | Allrights Reserved</span><span>Contact Us &nbsp;|&nbsp; Privacy Policy &nbsp;|&nbsp; Terms and Conditions</span></div>
</footer>

</body>
</html>
```